Wine Shop Banners

Banner graphic/images required
Require banner images to match the present online wine shop.

www.korbel-traube-laden.de

The wine-shop presently has a very clean, simple design, lots of white space, which is very much the trend at the moment.

Requirements
Images or graphic design for present banners visible on the homepage

The colour and feeling of the banners must fit in with the present clean, simple design.

Work required
3 large slide-card/banners (can be more) and 3 smaller fixed banners below. Please view website to see present position of banners.

LARGE BANNERS x 3

Something special with white background within the banner space
White background on each slide-card. Small individual graphic image in the middle of the slide card. This could be either a simple element of wine:
ingredients, fruit (grape), bottle, cork, old bottle label etc. just displaying one item on each slide-card. Preferably with high quality graphic features.

Note:
We are trying the steer away from the classic stereotype wineshop design. The image/s should have a higher, individual graphic touch, which gives the design something different. Sometimes such artistic work is displayed in steampunk or even in nostalgic design, which leaves the viewer slightly memorized with the content.
To clarify: we are not looking for a full steampunk design but possibly certain elements of this will give you an idea what we mean. That is to say, the design can go slightly in this direction without going over the top. Something small but very eye-catching.

SMALLER BANNERS x 3

One idea is:
Showing a symbol e.g. - discount sign "%" against a white background but again with a high graphic quality.

Target Market(s)

People interested in purchasing wine.
Ages approx. 25 to 65

Industry/Entity Type

Shop

Requirements
Must have
• Something special with white background
• Small individual graphic image in the middle of the slide card.
Nice to have
• The image/s should have a higher, individual graphic touch, which gives the design something different. Something that leaves the viewer slightly memorized with the content.
Should not have
• Not the typical classical design that is often seen on wine shops.

```html
<!DOCTYPE html>
<html lang="de">
<head>
<meta charset="utf-8">
<title>Lorental Weinhandel</title>
<link rel="stylesheet" href="https://fonts.googleapis.com/css2?family=Titillium+Web:wght@300;400&family=Great+Vibes&family=Cormorant+Garamond:ital,wght@1,400;1,500&family=Crimson+Text:wght@400&display=swap">
<style>
:root{
  --wine:#b0174a;
  --olive:#56602e;
  --lime:#d1dc5e;
  --lime-text:#d0d95e;
  --ink:#555;
  --muted:#999;
  --line:#e6e6e6;
  --script:#5a0f0a;
  --tan:#c8b89b;
  --brown:#7a6654;
  --badge:#bdc92a;
}
*{box-sizing:border-box;margin:0;padding:0}
html,body{width:1200px;height:766px;overflow:hidden;background:#fff}
body{position:relative;font-family:"Titillium Web",sans-serif;font-weight:300;color:var(--ink)}
.abs{position:absolute}

.brand{left:34px;top:34px;width:220px}
.brand-name{font-family:"Titillium Web",sans-serif;font-weight:400;font-size:42px;letter-spacing:1px;color:var(--olive);line-height:46px;display:flex;align-items:center;gap:8px}
.brand-name i{display:inline-block;width:12px;height:12px;background:var(--wine)}
.brand-tag{font-family:"Titillium Web",sans-serif;font-weight:400;font-size:14px;letter-spacing:5px;color:var(--olive);margin-top:6px}

.search{left:592px;top:52px;width:314px;height:36px;border:1px solid #aaa;display:flex}
.search svg{margin:9px 10px 0 12px}
.search span{font-size:15px;line-height:34px;color:#666;flex:1}
.search b{width:46px;background:var(--wine);color:#fff;font-weight:400;font-size:17px;text-align:center;line-height:34px}

.logout{left:1011px;top:38px;font-size:19px;color:#666}
.user{left:1112px;top:42px}

.nav{left:52px;top:136px;display:flex;font-size:20px;color:#666;line-height:30px}
.nav span{margin-right:41px}

.badge{width:19px;height:19px;border-radius:50%;background:var(--badge);color:#fff;font-size:12px;text-align:center;line-height:19px;font-weight:400}

.filter-head{left:33px;top:181px;width:233px;height:38px;background:var(--lime);color:var(--olive);font-weight:400;font-size:17px;line-height:38px;padding-left:13px}
.group{left:36px;font-size:17px;color:var(--lime-text);font-weight:400}
.list{left:36px;list-style:none;font-size:17px;color:#666;overflow:hidden}
.list li{height:25px;line-height:25px;display:flex;align-items:center}
.list li::before{content:"";width:5px;height:5px;border-right:1.3px solid #666;border-top:1.3px solid #666;transform:rotate(45deg);margin-right:9px}
.list em{font-style:normal;color:var(--muted);margin-left:4px}
.scroll{left:251px;top:266px;width:14px;height:182px;background:#eee}
.scroll i{position:absolute;left:1px;top:12px;width:12px;height:78px;background:#c8c8c8}

.slider{left:279px;top:179px;width:866px;height:341px;background:#fff;box-shadow:0 0 6px rgba(0,0,0,.18)}
.slogan{left:62px;top:70px;font-family:"Great Vibes",cursive;color:var(--script);font-size:96px;line-height:80px;transform:rotate(-4deg)}
.still-life{left:500px;top:26px;width:312px;height:315px;background:radial-gradient(ellipse at 60% 55%,#7a3a2a 0%,#3a2a18 30%,#c9a76a 60%,rgba(255,255,255,0) 78%)}
.dot{width:18px;height:18px;border-radius:50%;background:#fff;box-shadow:0 0 3px rgba(0,0,0,.45);top:300px}

.promo{top:529px;width:282px;height:134px;overflow:hidden;background:linear-gradient(90deg,#ececec,#fafafa 60%)}
.promo .panel{position:absolute;top:0;right:0;height:134px;width:190px;clip-path:polygon(28% 0,100% 0,100% 100%,0 100%)}
.promo .txt{position:absolute;font-family:"Cormorant Garamond",serif;font-style:italic;color:#555;line-height:1}
.promo .big{position:absolute;font-family:"Cormorant Garamond",serif;font-style:italic;color:#fff;line-height:1}
.promo .play{position:absolute;right:8px;bottom:8px}
.splash{left:0;top:0;width:200px;height:134px;background:radial-gradient(ellipse at 40% 40%,#d9cdb8,#f1ede6 60%,#fafafa)}

.section{left:306px;top:686px;font-family:"Crimson Text",serif;font-size:20px;color:#222}
.arrowbox{top:686px;width:19px;height:20px;border:1px solid #777}
.card{top:720px;width:216px;height:10px;border:1px solid var(--line);border-bottom:none;box-shadow:0 -2px 3px rgba(0,0,0,.05)}
.rule{left:274px;top:717px;width:876px;height:1px;background:#eee}
</style>
</head>
<body>

<header>
  <div class="abs brand">
    <div class="brand-name"><i></i>LORENTAL</div>
    <div class="brand-tag">WEINHANDEL</div>
  </div>

  <div class="abs search">
    <svg width="16" height="16" viewBox="0 0 16 16"><circle cx="6.5" cy="6.5" r="4.5" fill="none" stroke="#b0174a" stroke-width="2"/><line x1="10" y1="10" x2="14" y2="14" stroke="#b0174a" stroke-width="2.4"/></svg>
    <span>Suche</span><b>GO</b>
  </div>

  <div class="abs logout">Abmelden</div>
  <svg class="abs user" width="28" height="32" viewBox="0 0 28 32"><circle cx="14" cy="9" r="6.5" fill="none" stroke="#777" stroke-width="2"/><path d="M3 29 v-5 q0-6 11-6 q11 0 11 6 v5 z" fill="none" stroke="#777" stroke-width="2" stroke-linejoin="round"/></svg>

  <nav class="abs nav"><span>Rotwein</span><span>Weißwein</span><span>Rosewein</span><span>Sekt / Champagner</span><span>Sonderangebote</span><span>Probierpakete</span></nav>

  <svg class="abs" style="left:1046px;top:134px" width="32" height="28" viewBox="0 0 32 28"><path d="M1 3h5l4 15h16l3-11H8" fill="none" stroke="#777" stroke-width="2"/><circle cx="12" cy="23" r="2.5" fill="#777"/><circle cx="24" cy="23" r="2.5" fill="#777"/></svg>
  <div class="abs badge" style="left:1067px;top:127px">0</div>
  <svg class="abs" style="left:1106px;top:130px" width="34" height="34" viewBox="0 0 34 34"><circle cx="17" cy="17" r="17" fill="#8c8c8c"/><path d="M17 24 l-7-7 a4 4 0 0 1 7-5 a4 4 0 0 1 7 5 z" fill="none" stroke="#fff" stroke-width="2"/></svg>
  <div class="abs badge" style="left:1128px;top:126px">0</div>
</header>

<aside>
  <div class="abs filter-head">DETAILSUCHE</div>

  <div class="abs group" style="top:233px">LAND</div>
  <ul class="abs list" style="top:266px;height:182px">
    <li>Italien<em>(87)</em></li><li>Frankreich<em>(74)</em></li><li>Deutschland<em>(58)</em></li><li>Spanien<em>(35)</em></li><li>Südafrika<em>(15)</em></li><li>Österreich<em>(12)</em></li><li>Australien<em>(12)</em></li><li>Portugal<em>(10)</em></li>
  </ul>
  <div class="abs scroll"><i></i></div>

  <div class="abs group" style="top:469px">GESCHMACK</div>
  <ul class="abs list" style="top:503px">
    <li>Trocken<em>(303)</em></li><li>Halbtrocken<em>(8)</em></li><li>Lieblich<em>(5)</em></li><li>Süß<em>(3)</em></li><li>Edelsüss<em>(1)</em></li>
  </ul>

  <div class="abs group" style="top:649px">FARBE</div>
  <ul class="abs list" style="top:682px">
    <li>Rot<em>(155)</em></li><li>Weiß<em>(127)</em></li>
  </ul>
</aside>

<main>
  <section class="abs slider">
    <div class="abs slogan">Sweet or<br>&nbsp;&nbsp;Dry?</div>
    <div class="abs still-life" role="img" aria-label="Photo of a red and a white wine bottle, a wine glass, corks and a small barrel with red grapes"></div>
    <div class="abs dot" style="left:774px"></div>
    <div class="abs dot" style="left:805px"></div>
    <div class="abs dot" style="left:836px"></div>
  </section>

  <a class="abs promo" style="left:278px">
    <div class="panel" style="background:var(--tan)"></div>
    <div class="txt" style="left:26px;top:26px;font-size:25px;line-height:29px">free shipping<br>on orders<br>over</div>
    <div class="big" style="left:158px;top:34px;font-size:84px">$25</div>
    <svg class="play" width="22" height="22" viewBox="0 0 22 22"><circle cx="11" cy="11" r="10" fill="#fff"/><path d="M8.5 6.5l6 4.5-6 4.5z" fill="#444"/></svg>
  </a>

  <a class="abs promo" style="left:571px">
    <div class="abs splash" role="img" aria-label="Photo of a cork bursting from splashing sparkling wine"></div>
    <div class="panel" style="background:var(--brown)"></div>
    <div class="big" style="left:154px;top:50px;font-size:35px;line-height:29px">celebrate<br>in style</div>
    <svg class="play" width="22" height="22" viewBox="0 0 22 22"><circle cx="11" cy="11" r="10" fill="#fff"/><path d="M8.5 6.5l6 4.5-6 4.5z" fill="#444"/></svg>
  </a>

  <a class="abs promo" style="left:864px">
    <div class="panel" style="background:var(--brown)"></div>
    <div class="txt" style="left:26px;top:40px;font-size:40px;line-height:31px">special<br>offers</div>
    <div class="big" style="left:168px;top:22px;font-size:22px">save up to</div>
    <div class="big" style="left:146px;top:46px;font-size:78px">35%</div>
    <svg class="play" width="22" height="22" viewBox="0 0 22 22"><circle cx="11" cy="11" r="10" fill="#fff"/><path d="M8.5 6.5l6 4.5-6 4.5z" fill="#444"/></svg>
  </a>

  <svg class="abs" style="left:277px;top:687px" width="20" height="20" viewBox="0 0 20 20"><circle cx="10" cy="10" r="8.5" fill="none" stroke="#b0174a" stroke-width="1.5"/><path d="M8 6l5 4-5 4z" fill="#b0174a"/></svg>
  <h2 class="abs section" style="font-weight:400">Ausgewählte Produkte</h2>
  <svg class="abs arrowbox" style="left:1102px" viewBox="0 0 19 20"><path d="M11 6l-4 4 4 4" fill="none" stroke="#555" stroke-width="1.3"/></svg>
  <svg class="abs arrowbox" style="left:1126px" viewBox="0 0 19 20"><path d="M8 6l4 4-4 4" fill="none" stroke="#555" stroke-width="1.3"/></svg>

  <div class="abs rule"></div>
  <div class="abs card" style="left:274px"></div>
  <div class="abs card" style="left:494px"></div>
  <div class="abs card" style="left:714px"></div>
  <div class="abs card" style="left:934px"></div>
</main>

</body>
</html>
```